Business Card Design Project

We're looking for a unique business card design that stands out from the rest, using the brand and logo we've already developed.
Two-sided design please.
Orlenza Digital (www.orlenzadigital.example.au) is a digitally-focused advertising agency that has produces results-driven campaigns. As a result, we'd like our business card to reflect our innovative approach.
Size, shape, orientation, etc, are all flexible (providing the print costs don't become ridiculous or we have to sit there with tiny scissors!).
Business card should include space for name, title, email, mobile, landline and address.

```html
<!DOCTYPE html>
<html lang="en">
<head>
<meta charset="utf-8">
<title>Orlenza Digital — Business Card</title>
<link rel="stylesheet" href="https://fonts.googleapis.com/css2?family=Questrial&display=swap">
<style>
  :root {
    --brand-orange: #f46c1a;
    --brand-black: #000000;
    --paper: #ffffff;
    --ink-light: #ffffff;
    --ink-dark: #2a1a10;
    --mark-faint: rgba(255, 255, 255, 0.28);
  }
  html, body {
    margin: 0;
    padding: 0;
    width: 1200px;
    height: 714px;
    overflow: hidden;
    background: var(--paper);
  }
  .presentation {
    display: block;
    width: 1200px;
    height: 714px;
    font-family: "Questrial", "Century Gothic", sans-serif;
  }
  .card-body { fill: var(--brand-black); }
  .card-band { fill: var(--brand-orange); }
  .brand-dot { fill: var(--brand-orange); }
  .brand-dot--faint { fill: var(--mark-faint); }
  .front-name {
    fill: var(--ink-light);
    font-size: 74px;
    letter-spacing: 1px;
  }
  .front-tagline {
    fill: var(--ink-light);
    font-size: 22px;
    letter-spacing: 22px;
  }
  .back-company {
    fill: var(--brand-orange);
    font-size: 40px;
  }
  .back-title {
    fill: var(--ink-light);
    font-size: 34px;
    letter-spacing: 24px;
  }
  .back-label {
    fill: var(--ink-light);
    font-size: 23px;
  }
  .back-detail {
    fill: var(--ink-dark);
    font-size: 24px;
    letter-spacing: 0;
  }
  .back-contact {
    fill: var(--ink-dark);
    font-size: 19px;
    letter-spacing: 0;
  }
  .contact-icon { fill: var(--ink-light); }
  .contact-icon-line { fill: none; stroke: var(--ink-light); stroke-width: 1.4; }
</style>
</head>
<body>
<svg class="presentation" viewBox="0 0 1200 714" width="1200" height="714" xmlns="http://www.w3.org/2000/svg">

  <!-- Front of card -->
  <g class="card-front" transform="translate(91 418) rotate(-30.8)">
    <path class="card-body" d="M0,-177.5 H480 A177.5,177.5 0 0 1 480,177.5 H0 Z"/>
    <circle class="brand-dot" cx="495" cy="-8" r="100"/>
    <text class="front-name" x="200" y="18" text-anchor="middle">orlenza</text>
    <text class="front-tagline" x="210" y="66" text-anchor="middle">DIGITAL</text>
  </g>

  <!-- Back of card -->
  <g class="card-back">
    <path class="card-body" d="M1200,358 H743 A178,178 0 0 0 743,714 H1200 Z"/>
    <path class="card-band" d="M1200,460 H800 A127,127 0 0 0 800,714 H1200 Z"/>
    <circle class="brand-dot--faint" cx="952" cy="626" r="62"/>

    <text class="back-company" x="975" y="427" text-anchor="middle">Orlenza Digital</text>
    <text class="back-title" x="972" y="500" text-anchor="middle">TITLE</text>

    <text class="back-label" x="757" y="611">Address</text>
    <text class="back-detail" x="730" y="647" textLength="148" lengthAdjust="spacing">************</text>
    <text class="back-detail" x="730" y="669" textLength="148" lengthAdjust="spacing">************</text>
    <text class="back-detail" x="730" y="691" textLength="148" lengthAdjust="spacing">************</text>

    <!-- mobile -->
    <rect class="contact-icon-line" x="1023" y="612" width="6" height="11" rx="1"/>
    <text class="back-contact" x="1037" y="631" textLength="112" lengthAdjust="spacing">************</text>
    <!-- landline -->
    <path class="contact-icon" d="M1024,643 q2,-2 3,0 l1,3 q0,1 -1,2 q1,3 4,4 q1,-1 2,-1 l3,1 q2,1 0,3 q-2,2 -5,0 q-5,-3 -7,-7 q-2,-3 0,-5 z"/>
    <text class="back-contact" x="1037" y="659" textLength="112" lengthAdjust="spacing">************</text>
    <!-- email -->
    <rect class="contact-icon-line" x="1022" y="675" width="11" height="8"/>
    <path class="contact-icon-line" d="M1022,675 L1027.5,680 L1033,675"/>
    <text class="back-contact" x="1037" y="688" textLength="112" lengthAdjust="spacing">************</text>
  </g>
</svg>
</body>
</html>
```